Casa Vero Inspections Business Card

I need a business card for my new company. The company is going to provide home inspections. The name of the company is Casa Vero Inspections. I am not sure if I want a single sided card or a double. I have a logo already that I want to incorporate into the card design. I was wondering if I should incorporate a catch phrase on my card or not. If I did the phrase would be "The Intelligent Choice for Home Inspections" but i am unsure how or if to use it on a card. The following information needs to be on the card.
Home Inspection
My Name: Marcus T. Wolford Phone Number: 555-301-7762 Email: mwolford@casaveroinspections.com Website: www.casaveroinspections.com NY HI License # 27300519462

```html
<!DOCTYPE html>
<html lang="en">
<head>
<meta charset="utf-8">
<title>Casa Vero Inspections – Business Card</title>
<link rel="stylesheet" href="https://fonts.googleapis.com/css2?family=Montserrat:wght@700&family=Roboto:wght@400;500;700&display=swap">
<style>
  :root {
    --page-bg: #232325;
    --card-blue: #136aab;
    --card-dark: #212126;
    --accent-blue: #1a6cb8;
    --logo-light: #5eb2e8;
    --text-white: #f4f6f8;
  }
  * { box-sizing: border-box; margin: 0; padding: 0; }
  html, body { width: 1200px; height: 780px; overflow: hidden; }
  body {
    background: var(--page-bg);
    font-family: "Roboto", sans-serif;
    display: flex;
    align-items: center;
    justify-content: center;
    gap: 40px;
  }
  .card {
    width: 540px;
    height: 309px;
    border-radius: 18px;
    position: relative;
    overflow: hidden;
  }

  /* Front */
  .card-front {
    background: var(--card-blue);
    display: flex;
    align-items: center;
    justify-content: center;
  }
  .brand {
    display: flex;
    align-items: center;
    gap: 14px;
  }
  .brand-mark {
    width: 22px;
    height: 22px;
    background: var(--logo-light);
  }
  .brand-name {
    font-family: "Roboto", sans-serif;
    font-weight: 700;
    color: var(--logo-light);
    font-size: 34px;
    line-height: 1.05;
    letter-spacing: 0.5px;
  }
  .brand-name small { display: block; font-size: 34px; font-weight: 700; }

  /* Back */
  .card-back {
    background: var(--card-dark);
    border: 3px solid var(--accent-blue);
  }
  .back-brand {
    position: absolute;
    left: 30px;
    top: 82px;
  }
  .back-brand .brand-mark { width: 16px; height: 16px; background: var(--accent-blue); }
  .back-brand .brand-name { color: var(--accent-blue); font-size: 25px; }
  .back-brand .brand-name small { font-size: 25px; }
  .divider {
    position: absolute;
    left: 262px;
    top: 26px;
    width: 2px;
    height: 168px;
    background: var(--accent-blue);
  }
  .details {
    position: absolute;
    left: 282px;
    top: 30px;
    right: 16px;
    color: var(--text-white);
  }
  .person-name {
    font-family: "Montserrat", sans-serif;
    font-weight: 700;
    color: var(--accent-blue);
    font-size: 23px;
    line-height: 1.1;
  }
  .person-title {
    font-weight: 700;
    font-size: 12.5px;
    margin-top: 2px;
  }
  .license {
    margin-top: 16px;
    font-size: 12.5px;
  }
  .license-label { color: var(--accent-blue); }
  .contact-list { list-style: none; margin-top: 16px; }
  .contact-list li {
    display: flex;
    align-items: center;
    gap: 9px;
    font-size: 12.5px;
    margin-bottom: 7px;
  }
  .contact-list svg { width: 13px; height: 13px; flex: none; }
  .tagline-band {
    position: absolute;
    left: 0;
    right: 0;
    bottom: 22px;
    height: 36px;
    background: var(--accent-blue);
    color: var(--text-white);
    font-size: 14px;
    display: flex;
    align-items: center;
    justify-content: center;
  }
  .base-strip {
    position: absolute;
    left: 0;
    right: 0;
    bottom: 0;
    height: 22px;
    background: var(--card-dark);
  }
</style>
</head>
<body>
  <section class="card card-front" aria-label="Card front">
    <div class="brand">
      <span class="brand-mark"></span>
      <p class="brand-name">Casa Vero<small>Inspections</small></p>
    </div>
  </section>

  <section class="card card-back" aria-label="Card back">
    <div class="brand back-brand">
      <span class="brand-mark"></span>
      <p class="brand-name">Casa Vero<small>Inspections</small></p>
    </div>
    <div class="divider"></div>
    <div class="details">
      <h1 class="person-name">Marcus T. Wolford</h1>
      <p class="person-title">Managing Director</p>
      <p class="license"><span class="license-label">NY HI License #</span> 27300519462</p>
      <ul class="contact-list">
        <li>
          <svg viewBox="0 0 24 24" fill="var(--accent-blue)"><path d="M6.6 10.8a15 15 0 0 0 6.6 6.6l2.2-2.2a1 1 0 0 1 1-.25 11.4 11.4 0 0 0 3.6.57 1 1 0 0 1 1 1V20a1 1 0 0 1-1 1A17 17 0 0 1 3 4a1 1 0 0 1 1-1h3.5a1 1 0 0 1 1 1c0 1.25.2 2.45.57 3.6a1 1 0 0 1-.25 1z"/></svg>
          555-301-7762
        </li>
        <li>
          <svg viewBox="0 0 24 24" fill="none" stroke="var(--accent-blue)" stroke-width="2"><circle cx="12" cy="12" r="9"/><path d="M3 12h18M12 3c3 3.5 3 14.5 0 18M12 3c-3 3.5-3 14.5 0 18"/></svg>
          www.casaveroinspections.com
        </li>
        <li>
          <svg viewBox="0 0 24 24" fill="none" stroke="var(--accent-blue)" stroke-width="2"><rect x="3" y="6" width="18" height="13" rx="1"/><path d="M3 7l9 7 9-7"/></svg>
          mwolford@casaveroinspections.com
        </li>
      </ul>
    </div>
    <div class="tagline-band">The Intelligent Choice for Home Inspections</div>
    <div class="base-strip"></div>
  </section>
</body>
</html>
```